Dorin Commercial Truck / Trailer / RV Repair

Need a billboard design for our shop. Will include our logo below and want the word DORIN on the top without the circle. Straighten out the letter "M" on the logo as well. Also will include a rough draft of a design and words I had in mind. All the words need to be included but the layout and design is up to you. Open to all options just needs to be easy to see and understand the message from the highway.

```html
<!DOCTYPE html>
<html lang="en">
<head>
<meta charset="utf-8">
<title>Dorin Commercial Truck / Trailer / RV Repair – Billboard</title>
<link href="https://fonts.googleapis.com/css2?family=Montserrat:wght@700;800;900&display=swap" rel="stylesheet">
<style>
  :root {
    --page-bg: #e8edf2;
    --navy: #0b1a31;
    --brand-blue: #1a86d0;
    --white: #ffffff;
    --rule: #7d8796;
    --scene-sky: #9fc4dc;
    --scene-truck: #2f8fa3;
    --scene-road: #4b4f55;
  }
  html, body {
    margin: 0;
    width: 1200px;
    height: 1045px;
    overflow: hidden;
    background: var(--page-bg);
  }
  .canvas {
    position: relative;
    width: 1200px;
    height: 1045px;
    display: flex;
    align-items: center;
    justify-content: center;
  }
  .billboard {
    width: 1120px;
    height: 376px;
    display: block;
    box-shadow: 0 10px 30px rgba(11, 26, 49, 0.25);
    font-family: "Montserrat", sans-serif;
  }
  .brand-name { fill: var(--brand-blue); font-weight: 800; font-size: 136px; letter-spacing: 4px; }
  .service-list { fill: var(--white); font-weight: 800; font-size: 44px; letter-spacing: 1.5px; }
  .service-dot { fill: var(--brand-blue); }
  .headline { fill: var(--brand-blue); font-weight: 800; font-size: 46px; letter-spacing: 0.5px; }
  .subhead { fill: var(--white); font-weight: 800; font-size: 30px; letter-spacing: 3px; }
  .call-line { fill: var(--white); font-weight: 800; font-size: 25px; letter-spacing: 2px; }
  .phone-number { fill: var(--white); font-weight: 800; font-size: 58px; letter-spacing: 3px; }
  .rule { stroke: var(--rule); stroke-width: 2; }
</style>
</head>
<body>
<main class="canvas">
  <svg class="billboard" viewBox="0 0 1565 525" xmlns="http://www.w3.org/2000/svg" aria-label="Dorin commercial repair shop billboard">
    <defs>
      <linearGradient id="scene-fill" x1="0" y1="0" x2="0.3" y2="1">
        <stop offset="0" stop-color="var(--scene-sky)"/>
        <stop offset="0.45" stop-color="var(--scene-truck)"/>
        <stop offset="1" stop-color="var(--scene-road)"/>
      </linearGradient>
    </defs>

    <!-- navy message panel -->
    <rect class="panel" x="0" y="0" width="1565" height="525" fill="var(--navy)"/>

    <!-- accent stripe -->
    <polygon class="accent-stripe" points="983,0 1040,0 880,525 823,525" fill="var(--brand-blue)"/>

    <!-- photo area -->
    <g role="img" aria-label="Photo of a teal semi truck with a silver trailer driving on a highway">
      <polygon points="1040,0 1565,0 1565,525 840,525" fill="url(#scene-fill)"/>
    </g>

    <!-- brand name -->
    <text class="brand-name" x="150" y="155">DORIN</text>

    <!-- services -->
    <line class="rule" x1="60" y1="187" x2="745" y2="194"/>
    <text class="service-list" x="98" y="240">TRUCKS <tspan class="service-dot">•</tspan> TRAILERS <tspan class="service-dot">•</tspan> RV</text>
    <line class="rule" x1="60" y1="262" x2="745" y2="266"/>

    <!-- headline -->
    <text class="headline" x="50" y="323" textLength="704" lengthAdjust="spacingAndGlyphs">COMMERCIAL REPAIR SHOP</text>
    <text class="subhead" x="50" y="364" textLength="700" lengthAdjust="spacingAndGlyphs">PARKING AND STORAGE AVAILABLE</text>

    <!-- call to action -->
    <text class="call-line" x="100" y="432" textLength="528" lengthAdjust="spacingAndGlyphs">CALL OR COME BY FOR A QUOTE!</text>
    <polygon class="phone-band" points="0,440 732,448 700,525 0,525" fill="var(--brand-blue)"/>
    <g class="phone-icon" transform="translate(120,478)">
      <circle r="26" fill="var(--white)"/>
      <path d="M-10,-14 l6,-2 l5,10 l-4,4 q3,8 11,11 l4,-4 l10,5 l-2,6 q-4,5 -11,2 q-16,-7 -22,-22 q-2,-7 3,-10z" fill="var(--brand-blue)"/>
    </g>
    <text class="phone-number" x="162" y="499">888•555•0142</text>
  </svg>
</main>
</body>
</html>
```